Electrical Contracting Business Website

Require website done for my contracting business.
Partly done one but really dont have time.

You can view the current one at http://tolbran.net.au

You can use any info/styles/photos from the current website

I like the orange color of the logo so id like things to be with that
Unfortunatly being a new business (Sept 2015) I havent got alot of photos . but if you require any for any of the specifics listed in the doc file ill have a look to see what I have.

I am targeting mainly commercial / industrial clients. Which also includes government and mining.

Target Market(s)

People requiring electricians

Industry/Entity Type

Electrician

Coding

Coded - Design and coding required

Number of Pages Required

5+ page

Colors
f37122

Requirements
Must have
• logo with EC Number
• Keep it simple and not to complicated
• Comply with the current html / style sheet standards.
• Desktop/Mobile Version compatability
Nice to have
• additional photos.
• The domestic lifts we install are by vonrim I dont have any photos of them unfortunately.
Should not have
• change colour of logo

```html
<!DOCTYPE html>
<html lang="en">
<head>
<meta charset="utf-8">
<title>Tolbran Engineering – Electrical Contractor</title>
<link href="https://fonts.googleapis.com/css2?family=Mulish:wght@300;400;600;700&display=swap" rel="stylesheet">
<style>
:root{
  --orange:#f05a28;
  --white:#ffffff;
  --ink:#333333;
  --ink-soft:#666666;
  --hero-light:#fbfaf8;
  --hero-mid:#e4e2de;
  --hero-edge:#d6d3ce;
  --res-dark:#3a2a25;
  --res-mid:#6b4c42;
  --com-light:#f2f2f3;
  --com-mid:#dfe1e4;
  --ind-dark:#22272e;
  --ind-mid:#4a5360;
}
*{margin:0;padding:0;box-sizing:border-box}
html,body{width:1200px;height:2620px;overflow:hidden}
body{font-family:"Mulish",Arial,sans-serif;color:var(--ink);background:var(--white);position:relative}
.abs{position:absolute}

/* header */
.site-header{position:absolute;left:0;top:0;width:1200px;height:117px;background:var(--white);border-bottom:5px solid var(--orange)}
.brand{position:absolute;left:197px;top:38px;display:flex;align-items:center;gap:10px}
.brand-dot{width:34px;height:34px;border-radius:50%;background:var(--orange)}
.brand-name{font-size:32px;font-weight:700;color:var(--orange);letter-spacing:.5px}
.main-nav a{position:absolute;top:51px;font-size:14px;color:var(--ink);text-decoration:none}

/* hero */
.hero{left:0;top:122px;width:1200px;height:514px;
  background:
    radial-gradient(ellipse 240px 200px at 600px 150px,#ffffff 0%,rgba(255,255,255,.85) 55%,rgba(255,255,255,0) 100%),
    radial-gradient(ellipse 700px 360px at 600px 200px,var(--hero-light),var(--hero-mid) 70%,var(--hero-edge))}
.hero-arrow{top:364px;width:24px;height:34px}
.hero-kicker{left:0;width:1200px;top:476px;text-align:center;font-size:18px;color:var(--ink)}
.hero-title{left:0;width:1200px;top:496px;text-align:center;font-size:46px;font-weight:300;color:var(--orange)}
.services-tab{left:450px;top:571px;width:301px;height:65px}
.services-tab span{position:absolute;left:0;top:18px;width:301px;text-align:center;color:var(--white);font-size:22px;font-weight:300}

/* service bands */
.band{left:0;width:1200px}
.band-res{top:636px;height:451px;background:radial-gradient(ellipse at 70% 50%,var(--res-mid),var(--res-dark) 75%)}
.band-com{top:1087px;height:387px;background:linear-gradient(90deg,var(--com-mid),var(--com-light) 60%,var(--com-mid))}
.band-ind{top:1474px;height:383px;background:linear-gradient(90deg,var(--ind-dark),var(--ind-mid) 70%,var(--ind-dark))}
.photo-ring{width:230px;height:230px;border-radius:50%;border:7px solid var(--orange);padding:13px}
.photo-round{width:190px;height:190px;border-radius:50%}
.service-title{font-size:28px;font-weight:400;color:var(--orange)}
.service-list{list-style:none;font-size:13.5px;line-height:22.4px}
.service-list li{padding-left:44px;position:relative}
.service-list li::before{content:"›";position:absolute;left:0;font-size:16px}
.on-dark{color:var(--white)}
.on-light{color:var(--ink-soft)}
.on-light li::before{color:#aaa}

/* about */
.about-title{left:0;width:1200px;top:1925px;text-align:center;font-size:34px;font-weight:300;color:var(--orange)}
.about-tabs a{position:absolute;top:1999px;font-size:18px;font-weight:300;color:var(--ink);text-decoration:none}
.about-tabs a.is-active{border-bottom:2px solid var(--orange);padding-bottom:8px}
.video-frame{left:201px;top:2077px;width:388px;height:217px;background:#bbb;padding:6px;box-shadow:0 2px 6px rgba(0,0,0,.3)}
.video-still{width:376px;height:205px;background:linear-gradient(135deg,#8a97a6,#4d5a69 55%,#c6ccd3)}
.play{left:159px;top:73px}
.about-copy{left:610px;top:2106px;width:430px;font-size:10.5px;line-height:16px;color:var(--ink)}
.about-copy p+p{margin-top:12px}

/* footer */
.site-footer{left:0;top:2343px;width:1200px;height:277px;background:var(--orange)}
.foot-brand{position:absolute;left:197px;top:60px;display:flex;align-items:center;gap:8px}
.foot-brand .brand-dot{width:28px;height:28px;background:var(--white)}
.foot-brand .brand-name{color:var(--white);font-size:26px}
.foot-col{position:absolute;top:54px;list-style:none;font-size:10.5px;line-height:22.4px;color:var(--white)}
.partner-badge{position:absolute;left:910px;top:56px;width:107px;height:51px;background:var(--white)}
.copyright{position:absolute;left:0;width:1200px;top:245px;text-align:center;font-size:10.5px;color:var(--white)}
</style>
</head>
<body>

<header class="site-header">
  <div class="brand"><span class="brand-dot"></span><span class="brand-name">Tolbran</span></div>
  <nav class="main-nav">
    <a style="left:452px">Home</a>
    <a style="left:526px">About Us</a>
    <a style="left:620px">Residential</a>
    <a style="left:726px">Commercial</a>
    <a style="left:838px">Industrial</a>
    <a style="left:932px">Contact Us</a>
  </nav>
</header>

<section class="abs hero" role="img" aria-label="Photo of a white wall light switch and fan controller panel"></section>
<svg class="abs hero-arrow" style="left:88px" viewBox="0 0 24 34"><path d="M18 4 6 17l12 13" fill="none" stroke="#111" stroke-width="4"/></svg>
<svg class="abs hero-arrow" style="left:1088px" viewBox="0 0 24 34"><path d="M6 4l12 13L6 30" fill="none" stroke="#111" stroke-width="4"/></svg>
<div class="abs hero-kicker">Tolbran Engineering Pty Ltd</div>
<div class="abs hero-title">Electrical contractor</div>
<div class="abs services-tab">
  <svg width="301" height="65" viewBox="0 0 301 65"><path d="M14 0h273l14 65H0z" fill="var(--orange)"/></svg>
  <span>Our Services</span>
</div>

<!-- Residential -->
<section class="abs band band-res" role="img" aria-label="Close-up photo of hands stripping electrical wires"></section>
<div class="abs photo-ring" style="left:243px;top:779px">
  <div class="photo-round" style="background:radial-gradient(circle at 50% 40%,#f0eeeb,#cfd3d8)" role="img" aria-label="Photo of a smiling electrician in blue overalls"></div>
</div>
<h2 class="abs service-title" style="left:538px;top:812px">Residential Work</h2>
<ul class="abs service-list on-dark" style="left:542px;top:867px">
  <li>Domestic Lifts</li><li>Bore Pumps</li><li>Fault finding</li>
</ul>

<!-- Commercial -->
<section class="abs band band-com" role="img" aria-label="Faded photo of an electrician at a switchboard"></section>
<h2 class="abs service-title" style="left:201px;top:1186px">Commercial Work</h2>
<ul class="abs service-list on-light" style="left:200px;top:1259px">
  <li>Testing and tagging</li><li>Design &amp; Construct</li><li>Maintenance</li><li>Street lighting</li><li>Office and Shop fit outs</li>
</ul>
<ul class="abs service-list on-light" style="left:437px;top:1259px">
  <li>Generators</li><li>Data</li><li>CCTV</li><li>Automation</li><li>Labour Hire</li>
</ul>
<div class="abs photo-ring" style="left:704px;top:1158px">
  <div class="photo-round" style="background:radial-gradient(circle at 50% 40%,#9aa9ba,#5d6f84)" role="img" aria-label="Photo of a technician working on electrical equipment"></div>
</div>

<!-- Industrial -->
<section class="abs band band-ind" role="img" aria-label="Photo of a worker at an industrial control cabinet"></section>
<div class="abs photo-ring" style="left:243px;top:1527px">
  <div class="photo-round" style="background:radial-gradient(circle at 50% 40%,#6a7f97,#2f4259)" role="img" aria-label="Photo of an electrician holding a cable coil"></div>
</div>
<h2 class="abs service-title" style="left:550px;top:1548px">Industrial Work</h2>
<ul class="abs service-list on-dark" style="left:550px;top:1607px">
  <li>Design &amp; Construct</li><li>Maintenance</li><li>Tower Cranes</li><li>Gantry Cranes</li><li>Hoists</li><li>Dust collectors</li>
</ul>
<ul class="abs service-list on-dark" style="left:751px;top:1607px">
  <li>Fault finding</li><li>Generators</li><li>Automation and Control</li><li>Radio Control</li><li>Packaging Machines</li><li>Labour Hire</li>
</ul>

<!-- About -->
<h2 class="abs about-title">About Us</h2>
<nav class="about-tabs">
  <a class="is-active" style="left:360px">Our Values</a>
  <a style="left:515px">Safety</a>
  <a style="left:632px">Quality</a>
  <a style="left:756px">Reliability</a>
</nav>
<div class="abs video-frame">
  <div class="video-still" role="img" aria-label="Video still of hands wiring a switchboard"></div>
  <svg class="abs play" width="70" height="70" viewBox="0 0 70 70"><circle cx="35" cy="35" r="30" fill="none" stroke="var(--orange)" stroke-width="5"/><path d="M28 22v26l20-13z" fill="var(--orange)"/></svg>
</div>
<div class="abs about-copy">
  <p>Lorem ipsum dolor sit amet, consectetur adipiscing elit, sed do eiusmod tempor incididunt ut labore et dolore magna aliqua. Ut enim ad minim veniam, quis nostrud exercitation ullamco laboris nisi ut aliquip ex ea commodo consequat.</p>
  <p>Duis aute irure dolor in reprehenderit in voluptate velit esse cillum dolore eu fugiat nulla pariatur. Excepteur sint occaecat cupidatat non proident, sunt in culpa qui officia deserunt mollit anim id est laborum.</p>
</div>

<!-- Footer -->
<footer class="abs site-footer">
  <div class="foot-brand"><span class="brand-dot"></span><span class="brand-name">Tolbran</span></div>
  <ul class="foot-col" style="left:423px"><li>Home</li><li>About Us</li><li>Residential</li><li>Commercial</li><li>Industrial</li><li>Contact Us</li></ul>
  <ul class="foot-col" style="left:559px"><li>Term Of Service</li><li>Privacy Policy</li></ul>
  <ul class="foot-col" style="left:709px"><li>Contact Us should include</li><li>Email: info@tolbran.net.au</li><li>Phone: 0400 123 456</li><li>Fax: 08 5550 12 34</li></ul>
  <div class="partner-badge" role="img" aria-label="Industry association member badge"></div>
  <div class="copyright">Copyright © 2016 Tolbran Engineering Pty Ltd | All Rights Reserved</div>
</footer>

</body>
</html>
```